Plakat für Hersteller von Maultaschen und Knödeln
Zielgruppe
Mit meiner Manufaktur Rinnfalten & Co stelle ich Maultaschen und Knödel her. Produziert wird mit hochwertigen, möglichst regionalen Zutaten und mit dem Anspruch, traditionelle Klassiker in zeitgemäßer Qualität anzubieten.
Im Mittelpunkt stehen Frische, Transparenz und ehrliches Handwerk. Die Produkte werden mit Sorgfalt hergestellt und sind für den direkten Verkauf auf dem Brunnwaldener Wochenmarkt bestimmt. Rinnfalten & Co verbindet bodenständige Küche mit regionaler Identität – unkompliziert, authentisch und genussorientiert.
Zielgruppe rund um den Brunnwaldener Wochenmarkt:
- Marktbesucher mit Qualitätsbewusstsein, die gezielt regionale und handwerklich hergestellte Lebensmittel kaufen
- Berufstätige und Familien, die hochwertige, frisch produzierte Gerichte für zu Hause suchen
- Genussorientierte Kundinnen und Kunden, die traditionelle Küche schätzen
- Seniorinnen und Senioren, die klassische Hausmannskost bevorzugen
- Regionalverbundenen Verbraucherinnen und Verbrauchern, die lokale Anbieter unterstützen möchten
Der Brunnwaldener Wochenmarkt zieht ein vielfältiges Publikum an, das Wert auf persönliche Beratung, Frische und nachvollziehbare Herkunft legt. Rinnfalten positioniert sich hier als authentischer, spezialisierter Anbieter für handgemachte Teigklassiker mit klarem kulinarischem Profil.
Aufgabenstellung
Das Plakat soll in A5, A4, A3 und A2 nutzbar sein und der Text soll austauschbar sein.
Das Plakat soll gut zum Wochenmarkt passen und ehrliches, qualitativ hochwertiges Handwerk ausdrücken und vor allem Lust auf Maultaschen und Knödel machen. Es soll zu meinen Marktstand (Monza Rot) und dem Logo passen. Das Logo soll sehr präsent sein.

```html
<!DOCTYPE html>
<html lang="de">
<head>
<meta charset="utf-8">
<title>Rinnfalten &amp; Co – Plakat</title>
<link rel="stylesheet" href="https://fonts.googleapis.com/css2?family=Arimo:wght@400;700&display=swap">
<style>
  :root {
    --stage: #f1f1f1;
    --paper: #ffffff;
    --monza-red: #b01721;
    --text-light: #ffffff;
    --brand-accent: #e6d27a;
    --dumpling-light: #eee2b0;
    --dumpling-mid: #d8c27c;
    --dumpling-deep: #c9a95c;
  }
  * { margin: 0; padding: 0; box-sizing: border-box; }
  html, body {
    width: 696px;
    height: 1200px;
    overflow: hidden;
    background: var(--stage);
    font-family: "Arimo", Arial, sans-serif;
  }
  .poster {
    position: absolute;
    left: 20px;
    top: 134px;
    width: 656px;
    height: 931px;
    background: var(--paper);
    box-shadow: 0 10px 40px rgba(0, 0, 0, 0.18);
    overflow: hidden;
  }
  .poster-field {
    position: absolute;
    left: 22px;
    top: 22px;
    width: 612px;
    height: 886px;
    background: var(--monza-red);
  }
  .brand {
    position: absolute;
    left: 0;
    top: 78px;
    width: 656px;
    display: flex;
    justify-content: center;
    align-items: center;
    gap: 20px;
  }
  .brand-dot {
    width: 78px;
    height: 78px;
    border-radius: 50%;
    background: var(--brand-accent);
    flex: none;
  }
  .brand-name {
    font-size: 56px;
    line-height: 1;
    font-weight: 700;
    color: var(--text-light);
    letter-spacing: -0.5px;
    white-space: nowrap;
  }
  .message {
    position: absolute;
    left: 0;
    top: 280px;
    width: 656px;
    text-align: center;
    color: var(--text-light);
  }
  .headline {
    font-size: 31px;
    line-height: 40px;
    font-weight: 400;
  }
  .headline strong { font-weight: 700; }
  .subline {
    margin-top: 34px;
    font-size: 23px;
    line-height: 30px;
    font-weight: 400;
  }
  .product-visual {
    position: absolute;
    left: 0;
    top: 560px;
    width: 436px;
    height: 356px;
    background: linear-gradient(180deg, var(--dumpling-light) 0%, var(--dumpling-mid) 60%, var(--dumpling-deep) 100%);
  }
</style>
</head>
<body>
  <main class="poster">
    <div class="poster-field"></div>

    <header class="brand">
      <span class="brand-dot"></span>
      <span class="brand-name">Rinnfalten &amp; Co</span>
    </header>

    <section class="message">
      <h1 class="headline"><strong>Maultaschen und Knödel.</strong><br>Handgemachte Klassiker,<br>jede Woche frisch.</h1>
      <p class="subline">Zum Mitnehmen für zu Hause oder<br>heiß und lecker direkt vor Ort.</p>
    </section>

    <div class="product-visual" role="img" aria-label="Foto: drei Semmelknödel mit Petersilie und gerösteten Bröseln"></div>
  </main>
</body>
</html>
```